Join us at the Maple Ridge Splashpark Lodge for July 4th Fun!

On the fourth of July which is a Wednesday, we will be having many extra fun activities for guests at the waterpark.

we would like you to come up with a quick but fun graphic for Facebook and website to advertise it and a flyer that is elevator size ( 11 x 17)

1. Complimentary face painting.
2. Cornhole tournaments.
3. Free popsicles.
4. "Guess the amount" candy jar contest.
5. Complimentary photo booth and picture by Snapfolio -> https://www.facebook.com/grinframestudio/

I have attached logos & examples of current advertisements as this should stay in brand

website is www.MapleRidgeSplash.com
FB https://www.facebook.com/MapleRidgeSplash/

Target Market(s)

Guest and potential guest to join us at the poolside for fun July 4th events

Industry/Entity Type

Hospitality

Requirements
Must have
• Logo and be consistent with the attached examples of branded items

```html
<!DOCTYPE html>
<html lang="en">
<head>
<meta charset="utf-8">
<title>Maple Ridge Splashpark Lodge – July 4th</title>
<link href="https://fonts.googleapis.com/css2?family=Arimo:wght@400;700&family=Libre+Baskerville:ital,wght@1,700&family=Alfa+Slab+One&display=swap" rel="stylesheet">
<style>
  :root {
    --stage: #e9e7e3;
    --header-bg: #f1f1fa;
    --navy: #3b3f92;
    --navy-deep: #2e3280;
    --ink: #1f2a6b;
    --orange: #f47b30;
    --nav-text: #f2b48a;
    --sky-top: #3f7fd0;
    --sky-low: #cfe3f5;
    --white: #ffffff;
    --blue-btn: #2a8ee0;
    --badge-red: #8c2a1c;
    --badge-gold: #d9a233;
    --snack: #7fc2ea;
  }
  * { box-sizing: border-box; margin: 0; padding: 0; }
  html, body { width: 1200px; height: 797px; overflow: hidden; background: var(--stage); }
  .site { position: absolute; left: 0; top: 61px; width: 1200px; height: 674px; background: var(--white); font-family: 'Arimo', sans-serif; }
  .site-header { position: absolute; left: 0; top: 0; width: 1200px; height: 135px; background: var(--header-bg); }
  .brand { position: absolute; left: 258px; top: 28px; display: flex; align-items: center; gap: 12px; }
  .brand-dot { width: 44px; height: 44px; border-radius: 50%; background: var(--navy); }
  .brand-name { font-family: 'Arimo', sans-serif; font-weight: 700; color: var(--ink); font-size: 24px; line-height: 1.15; }
  .phone { position: absolute; left: 873px; top: 63px; font-size: 21px; color: var(--ink); }
  .main-nav { position: absolute; left: 0; top: 135px; width: 1200px; height: 46px; background: var(--navy); }
  .main-nav a { position: absolute; top: 15px; font-size: 15px; letter-spacing: 1px; color: var(--nav-text); text-decoration: none; }
  .main-nav .book { top: 4px; left: 944px; width: 241px; height: 40px; background: var(--orange); color: var(--ink); text-align: center; line-height: 40px; }
  .banner { position: absolute; left: 0; top: 181px; width: 1200px; height: 447px; background: var(--navy); }
  .promo { position: absolute; left: 4px; top: 5px; width: 529px; height: 320px; background: linear-gradient(170deg, var(--sky-top), var(--sky-low) 75%, var(--white)); }
  .promo-name { position: absolute; left: 18px; top: 16px; width: 300px; font-family: 'Arimo', sans-serif; font-weight: 700; font-size: 26px; line-height: 1.1; color: var(--ink); }
  .events { position: absolute; left: 14px; top: 143px; list-style: none; font-family: 'Libre Baskerville', serif; font-style: italic; font-weight: 700; font-size: 19px; line-height: 29px; color: var(--ink); }
  .events li { padding-left: 24px; text-indent: -24px; width: 510px; }
  .photo { position: absolute; top: 5px; height: 320px; }
  .photo-play { left: 544px; width: 311px; background: linear-gradient(180deg, #6a8f4c, #c6d07a 45%, #8fd3e6); }
  .photo-pool { left: 866px; width: 314px; background: linear-gradient(180deg, #9cc2e8, #a0785c 40%, #56b9d8 70%, #84cde4); }
  .strip-badge { position: absolute; }
  .badge-breakfast { left: 13px; top: 338px; width: 148px; height: 104px; border-radius: 50%; background: var(--badge-red); }
  .badge-years { left: 179px; top: 336px; width: 106px; height: 106px; border-radius: 50%; background: var(--badge-gold); }
  .snack-name { position: absolute; left: 306px; top: 373px; width: 220px; font-size: 26px; line-height: 32px; font-weight: 700; color: var(--snack); white-space: nowrap; }
  .invite { position: absolute; left: 622px; top: 341px; font-family: 'Libre Baskerville', serif; font-style: italic; font-weight: 700; font-size: 19px; line-height: 27px; color: var(--white); white-space: nowrap; }
  .date { position: absolute; left: 815px; top: 346px; font-family: 'Alfa Slab One', serif; font-size: 44px; line-height: 48px; color: var(--white); }
  .slider { position: absolute; left: 540px; top: 398px; display: flex; gap: 4px; }
  .slider span { width: 34px; height: 38px; background: var(--orange); display: flex; align-items: center; justify-content: center; }
  .slider .current { background: var(--blue-btn); }
</style>
</head>
<body>
<div class="site">
  <header class="site-header">
    <div class="brand">
      <span class="brand-dot"></span>
      <span class="brand-name">Maple Ridge<br>Splashpark Lodge</span>
    </div>
    <div class="phone">1-800-555-0147</div>
  </header>
  <nav class="main-nav">
    <a style="left:124px">Guest Rooms</a>
    <a style="left:367px">Waterpark</a>
    <a style="left:594px">Discounts</a>
    <a style="left:824px">Recreation</a>
    <a class="book">Book Now!</a>
  </nav>
  <section class="banner">
    <div class="promo" role="img" aria-label="Blue summer sky with white clouds">
      <div class="promo-name">Maple Ridge<br>Splashpark Lodge</div>
      <ol class="events">
        <li>1. Complimentary face painting.</li>
        <li>2. Cornhole tournaments.</li>
        <li>3. Free popsicles.</li>
        <li>4. "Guess the amount" candy jar contest.</li>
        <li>5. Complimentary photo booth and picture by Snapfolio</li>
      </ol>
    </div>
    <div class="photo photo-play" role="img" aria-label="Children playing on the splash play structure"></div>
    <div class="photo photo-pool" role="img" aria-label="Outdoor pool with water slides in front of the lodge"></div>
    <div class="strip-badge badge-breakfast"></div>
    <div class="strip-badge badge-years"></div>
    <div class="snack-name">Poolside Snacks</div>
    <div class="slider">
      <span class="current"><svg width="10" height="12" viewBox="0 0 10 12"><path d="M8 1 2 6l6 5" fill="none" stroke="#fff" stroke-width="2"/></svg></span>
      <span><svg width="10" height="12" viewBox="0 0 10 12"><path d="M2 1v10l7-5z" fill="#2e3280"/></svg></span>
      <span><svg width="10" height="12" viewBox="0 0 10 12"><path d="M2 1l6 5-6 5" fill="none" stroke="#fff" stroke-width="2"/></svg></span>
    </div>
    <div class="invite">join us at the<br>poolside for fun</div>
    <div class="date">July 4th<br>2018</div>
  </section>
</div>
</body>
</html>
```